TR REFEREE ADVISORY sports

Require a banner for a website titled:

TR REFEREE ADVISORY

A sporting style banner to support referees / umpires

using some of the images listed below.

Require a new logo
I do not have a logo for this as yet.

Need to be able to use it on webpages as well.

Thanks Owen

Target Market(s)

SPORT CLUBS / INDIVIDUAL REFEREES / OFFICIALS

Logo Text

TR REFEREE ADVISORY

Font styles to use
Sans Serif

Colors
3277b5

Requirements
Must have
• TAGLINE - SHAPING YOUR CAREER

```html
<!DOCTYPE html>
<html lang="en">
<head>
<meta charset="utf-8">
<title>TR Referee Advisory – Banner and Logo</title>
<link rel="stylesheet" href="https://fonts.googleapis.com/css2?family=Open+Sans:ital,wght@0,600;0,700;0,800;1,600&display=swap">
<style>
  :root {
    --page-bg: #f1f1f1;
    --brand-blue: #3277b5;
    --brand-blue-deep: #1d5686;
    --brand-blue-dark: #174a74;
    --white: #ffffff;
    --photo-coach: #4d6a5c;
    --photo-handshake: #7a4638;
    --photo-court: #5f7d5e;
    --photo-crowd: #8b7d66;
    --photo-portrait: #5a5f66;
    --divider: #c9ced3;
  }
  * { margin: 0; padding: 0; box-sizing: border-box; }
  html, body { width: 1200px; height: 1200px; overflow: hidden; }
  body {
    background: radial-gradient(ellipse at 50% 45%, #fbfbfb 0%, var(--page-bg) 70%, #e6e6e6 100%);
    font-family: 'Open Sans', Arial, sans-serif;
    position: relative;
  }
  .banner {
    position: absolute;
    left: 120px; top: 375px;
    width: 959px; height: 325px;
    box-shadow: 0 2px 6px rgba(0,0,0,0.18);
  }
  .banner-art { position: absolute; inset: 0; width: 100%; height: 100%; display: block; }
  .portrait {
    position: absolute;
    left: 142px; top: 394px;
    width: 140px; height: 140px;
    border-radius: 50%;
    border: 6px solid var(--white);
    background: radial-gradient(circle at 50% 40%, #7b8189, var(--photo-portrait) 70%);
  }
  .banner-brand {
    position: absolute;
    left: 312px; top: 402px;
    width: 180px;
    color: var(--white);
    font-weight: 800;
    text-align: center;
  }
  .banner-brand .brand-initials { display: block; font-size: 58px; line-height: 64px; letter-spacing: 1px; }
  .banner-brand .brand-words { display: block; font-size: 11px; letter-spacing: 1.4px; margin-top: 2px; }
  .tagline {
    position: absolute;
    left: 282px; top: 506px;
    color: var(--white);
    font-size: 21px;
    font-weight: 600;
    font-style: italic;
  }
  .contact {
    position: absolute;
    left: 170px; top: 568px;
    width: 285px;
    text-align: center;
    color: var(--white);
    font-weight: 700;
  }
  .contact .call-label { font-size: 19px; line-height: 24px; }
  .contact .phone { font-size: 25px; line-height: 34px; display: flex; align-items: center; justify-content: center; gap: 10px; }
  .contact .phone svg { width: 26px; height: 26px; }
  .contact .email { font-size: 15px; line-height: 28px; font-weight: 600; }
  .logo {
    position: absolute;
    left: 450px; top: 800px;
    width: 300px;
    text-align: center;
    color: var(--brand-blue-deep);
    font-weight: 800;
  }
  .logo .brand-initials { display: block; font-size: 72px; line-height: 76px; letter-spacing: 2px; }
  .logo .brand-words { display: block; font-size: 13px; letter-spacing: 1.6px; }
</style>
</head>
<body>
  <section class="banner" aria-label="TR Referee Advisory website banner">
    <svg class="banner-art" viewBox="0 0 959 325" preserveAspectRatio="none" aria-hidden="false">
      <defs>
        <linearGradient id="banner-blue" x1="0" y1="0" x2="1" y2="1">
          <stop offset="0" stop-color="var(--brand-blue-deep)"/>
          <stop offset="0.55" stop-color="var(--brand-blue)"/>
          <stop offset="1" stop-color="var(--brand-blue-dark)"/>
        </linearGradient>
        <clipPath id="photo-window">
          <path d="M478,0 H955 C945,150 905,265 838,325 H383 C398,200 428,85 478,0 Z"/>
        </clipPath>
      </defs>
      <rect class="banner-bg" width="959" height="325" fill="url(#banner-blue)"/>
      <g clip-path="url(#photo-window)">
        <rect x="370" y="0" width="280" height="185" fill="var(--photo-coach)" role="img" aria-label="Photo: tennis umpire in the chair"/>
        <rect x="650" y="0" width="309" height="185" fill="var(--photo-handshake)" role="img" aria-label="Photo: rugby referee signalling beside players"/>
        <rect x="370" y="185" width="280" height="140" fill="var(--photo-court)" role="img" aria-label="Photo: netball players and umpire on court"/>
        <rect x="650" y="185" width="309" height="140" fill="var(--photo-crowd)" role="img" aria-label="Photo: cricket umpires with batsman"/>
        <line x1="650" y1="0" x2="650" y2="325" stroke="var(--divider)" stroke-width="3"/>
        <line x1="370" y1="185" x2="959" y2="185" stroke="var(--divider)" stroke-width="3"/>
      </g>
      <path d="M478,0 C428,85 398,200 383,325" fill="none" stroke="var(--white)" stroke-width="8"/>
      <path d="M955,0 C945,150 905,265 838,325" fill="none" stroke="var(--white)" stroke-width="4"/>
    </svg>
  </section>

  <div class="portrait" role="img" aria-label="Portrait photo of Owen"></div>

  <div class="banner-brand">
    <span class="brand-initials">TR</span>
    <span class="brand-words">REFEREE ADVISORY</span>
  </div>

  <p class="tagline">Shaping Your Career</p>

  <div class="contact">
    <p class="call-label">CALL US:</p>
    <p class="phone">
      <svg viewBox="0 0 24 24" aria-hidden="true"><path fill="#ffffff" d="M6.6 10.8c1.4 2.8 3.8 5.1 6.6 6.6l2.2-2.2c.3-.3.7-.4 1-.2 1.1.4 2.3.6 3.6.6.6 0 1 .4 1 1V20c0 .6-.4 1-1 1C10.6 21 3 13.4 3 4c0-.6.4-1 1-1h3.5c.6 0 1 .4 1 1 0 1.3.2 2.5.6 3.6.1.3 0 .7-.2 1z"/></svg>
      0400 555 318
    </p>
    <p class="email">owen@trrefereeadvisory.com.au</p>
  </div>

  <div class="logo" aria-label="TR Referee Advisory">
    <span class="brand-initials">TR</span>
    <span class="brand-words">REFEREE ADVISORY</span>
  </div>
</body>
</html>
```